Bakery Business Cards

We are in need of business cards for our bakery business--something non-generic that reflects our business and will stand out. We are a wholesale bakery that primarily services in-store bakeries, casinos, schools, distributors, and fund-raising companies. The family business was founded in 1960. (www.marlowsovenworks.com)

```html
<!DOCTYPE html>
<html lang="en">
<head>
<meta charset="utf-8">
<title>Marlow's Ovenworks – Business Cards</title>
<link href="https://fonts.googleapis.com/css2?family=Montserrat:wght@500;600;700&display=swap" rel="stylesheet">
<style>
  :root {
    --backdrop: #d8d8d6;
    --berry-body: #6a0c10;
    --berry-crust: #911a1f;
    --pastry-body: #efb75e;
    --pastry-crust: #dd8b3c;
    --ink-light: #ffffff;
    --ink-brand: #a3181f;
  }
  html, body {
    margin: 0;
    padding: 0;
    overflow: hidden;
  }
  .canvas {
    position: relative;
    width: 1200px;
    height: 900px;
    background: var(--backdrop);
    overflow: hidden;
    font-family: "Montserrat", sans-serif;
  }
  .cards {
    position: absolute;
    inset: 0;
  }
  .card-edge { fill: #2a2a2a; opacity: 0.35; }
  .back-crust { fill: var(--berry-crust); }
  .back-body { fill: var(--berry-body); }
  .front-crust { fill: var(--pastry-crust); }
  .front-body { fill: var(--pastry-body); }

  .contact {
    position: absolute;
    color: var(--ink-light);
    font-weight: 600;
    font-size: 14px;
    letter-spacing: -0.2px;
    line-height: 1.25;
    text-align: center;
    white-space: nowrap;
    transform: translate(-50%, -50%) rotate(-18deg);
  }
  .contact-icon {
    position: absolute;
    transform: translate(-50%, -50%) rotate(-18deg);
  }
  .contact-icon svg { display: block; fill: var(--ink-light); }

  .brand-name {
    position: absolute;
    left: 906px;
    top: 318px;
    transform: translate(-50%, -50%) rotate(-10deg);
    color: var(--ink-brand);
    font-weight: 700;
    font-size: 34px;
    line-height: 1.1;
    text-align: center;
    white-space: nowrap;
  }
</style>
</head>
<body>
<main class="canvas">
  <svg class="cards" width="1200" height="900" viewBox="0 0 1200 900" aria-hidden="true">
    <defs>
      <clipPath id="back-shape">
        <path d="M111,192 Q118,162 190,140 Q380,58 470,50 Q506,54 507,110 L484,735 Q480,752 462,751 Q449,749 440,735 L115,215 Q106,202 111,192 Z"/>
      </clipPath>
      <clipPath id="front-shape">
        <path d="M684,262 Q690,234 740,222 Q900,190 1060,184 Q1092,188 1092,216 L1036,830 Q1031,849 1014,849 Q1002,847 994,834 L690,285 Q682,273 684,262 Z"/>
      </clipPath>
    </defs>

    <!-- back side: contact card -->
    <path class="card-edge" transform="translate(2,3)" d="M111,192 Q118,162 190,140 Q380,58 470,50 Q506,54 507,110 L484,735 Q480,752 462,751 Q449,749 440,735 L115,215 Q106,202 111,192 Z"/>
    <g clip-path="url(#back-shape)">
      <rect class="back-crust" x="90" y="40" width="440" height="730"/>
      <path class="back-body" d="M100,206 L118,192 C135,178 150,186 165,172 C185,154 200,166 220,150 C245,130 262,146 285,126 C300,112 318,124 340,112 C365,98 382,110 405,99 C425,90 440,98 458,92 C478,86 490,96 500,106 L510,112 L510,800 L100,800 Z"/>
    </g>

    <!-- front side: brand card -->
    <path class="card-edge" transform="translate(2,3)" d="M684,262 Q690,234 740,222 Q900,190 1060,184 Q1092,188 1092,216 L1036,830 Q1031,849 1014,849 Q1002,847 994,834 L690,285 Q682,273 684,262 Z"/>
    <g clip-path="url(#front-shape)">
      <rect class="front-crust" x="670" y="170" width="440" height="700"/>
      <path class="front-body" d="M680,282 L694,266 C710,252 722,262 736,248 C755,232 770,244 790,230 C812,214 828,228 850,212 C868,200 885,210 905,200 C930,190 945,200 968,192 C990,186 1005,194 1025,188 C1048,182 1062,190 1078,196 L1095,206 L1095,870 L680,870 Z"/>
    </g>
  </svg>

  <!-- contact details on back -->
  <div class="contact-icon" style="left:329px; top:215px;">
    <svg width="14" height="18" viewBox="0 0 14 18"><path d="M7 0C3.1 0 0 3 0 6.8 0 11.5 7 18 7 18s7-6.5 7-11.2C14 3 10.9 0 7 0zm0 9.4A2.6 2.6 0 1 1 7 4.2a2.6 2.6 0 0 1 0 5.2z"/></svg>
  </div>
  <div class="contact" style="left:350px; top:276px;">Marlow's Ovenworks, Inc.<br>1875 Fallow Ave<br>Brookhaven, OK 73199</div>

  <div class="contact-icon" style="left:361px; top:339px;">
    <svg width="22" height="15" viewBox="0 0 22 15"><path d="M0 0h22L11 8.5z"/><path d="M0 2l11 8.5L22 2v13H0z"/></svg>
  </div>
  <div class="contact" style="left:378px; top:370px;">contact@marlowsovenworks.com</div>

  <div class="contact-icon" style="left:382px; top:419px;">
    <svg width="16" height="22" viewBox="0 0 16 22"><path d="M3 0l3 1.2-.6 5.5-2.6.8c.3 3.6 2 6.9 4.6 9.3l2.3-1.5 4.4 3.4-1.6 2.8C6.5 21 .2 13.4 0 3.2z"/></svg>
  </div>
  <div class="contact" style="left:393px; top:455px;">405.555.0187</div>

  <!-- brand name on front -->
  <div class="brand-name">Marlow's<br>Ovenworks</div>
</main>
</body>
</html>
```